VORELLE Body Scrub and Lotion Label Design

Need designs for new product line, VORELLE, for a day spa in Houston, TX. We are a Japanese inspired day spa and have been opened for 26 years. We are currently in the process of creating a product line of body scrubs and lotions. The product line represent scents based on the 5 Japanese elements hi (Fire), kaze (Wind), tsuchi (Earth), mizu (Water), and sora (Heaven). The final design should have a cohesive Japanese influence and each label should represent the corresponding element. I will need a 3 inch label for the cap of the jar with name, ingredients, design and size. A 3 inch label for description and instruction on use of product on bottom of jar, a wrap around label for jar with the name of the product & description and size, and a full wrap around label for lotion bottles. Below are the links for each of the containers and jar cap.

Jar - https://www.jarbinstocksupply.com/item/J049A
Jar cap - https://www.jarbinstocksupply.com/item/L252
Bottle - https://www.jarbinstocksupply.com/item/B320A

Description for each element for design inspiration:
火 hi (Fire) - Evoking thoughts of cozying up with a warm cup of chai on a cool autumn night, our 火 hi (Fire) Cleansing Body Scrub embodies the virtue of purity while delivering a decadent experience. Organic Japanese honey crystals, organic Japanese black tea and organic sunflower seed oil, exfoliate and renew parched, rough skin while powerful essential oils increase circulation and flush toxins from the skin. Japanese honey, which contains antibacterial, antiseptic, and antioxidant properties, heals and nourishes while glycolic acid, one of honey’s natural alpha hydroxy acids, exfoliates and smooths the skin. As a humectant, honey also revitalizes and soothes overworked, dehydrated skin. Together these powerful ingredients support the skin’s own cell renewal process, and assist in creating smooth, hydrated skin. Renew, smooth, and revive the natural glow of youthful skin with 火 hi (Fire) Cleansing Body Scrub.

Use: Grab a small amount. Massage gently onto surface of dry skin. Add a small amount of warm water and massage gently again. Rinse with warm water, dry and apply 火 hi (Fire) Body Lotion.

Ingredients: Sucrose (Organic Sugar), Organic Helianthus Annuus (Sunflower) Seed Oil, Organic Honey Crystals (Dried Honey, Cane Juice and Molasses), Organic Camellia Sinensis (Black Tea), Mel (Honey), Citrus Medica Limonum (Lemon) Peel Oil, Citrus Junos (Yuzu) Peel Oil, Eucalyptus Globules Leaf Oil, Eugenia Caryophyllus (Clove) Flower Oil, Cinnamonum Zeylanicum (Cinnamon) Leaf Oil, Rosmarinus Officinalis (Rosemary) Leaf Oil, Tocopherol (Vitamin E).
___________________________

風 kaze (Wind) - Rouse your senses and renew your dull skin with 風 kaze (Wind) Body Scrub. Pure Asian Sea salt and Israeli Dead Sea salt, along with Japanese fruit powders, gently exfoliate to reveal fresher, more vibrant skin. Sweet almond, lavender, and clary sage oils soothe body and mind as lemon peel and oils of rosemary and cajeput heal and improve skin clarity. 風 kaze (Wind) Cleansing Body Scrub also helps protects skin from environmental damage (including UV rays) with the powerful antioxidant, vitamin E. Prepare to show skin that glows with 風 kaze (Wind) Cleansing Body Scrub.

Use: Grab a small amount. Massage gently onto surface of dry skin. Add a small amount of warm water and massage gently again. Rinse with warm water, dry and apply 風 kaze (Wind) Body Lotion.

Ingredients: Sodium Chloride (Asian Sea and Israeli Dead Sea Salt), Prunus Amygdalus Dulcis (Sweet Almond) Oil, Lavandula Angustifolia (Lavender) Buds, Rosmarinus Officinalis (Rosemary) Leaf Oil, Citrus Medica Limonum (Lemon) Peel Powder, Citrus Junos (Yuzu) Peel Oil, Melaleuca Cajeputi (Cajeput) Oil, Lavandula Angustifolia (Lavender) Oil, Luffa Cylindrica (Luffa) Fruit Powder, Salvia Sclarea (Clary) Oil, Baphicacanthus Cusia (Nees) Bremek Powder, Tocopherol (Vitamin E).
____________________________

地 tsuchi (Earth) - Imagine yourself surrounded by the beauty of a Japanese sacred grove as your body is cleansed and restored to its natural glowing state with the garden-inspired 地 tsuchi (Earth) Cleansing Body Scrub. Himalayan Pink Salts are organic compliant and hand-mined from deep within the Himalayan Mountains. Himalayan Pink Salts were crystallized more than 200 million years ago, when ancient sea beds were covered by volcanic lava, protecting the salt from modern-day pollution and lending to the belief that it is the purest salt to be found on earth. These ancient salts, along with dried blue cornflowers, jasmine flowers and lavender buds, exfoliate dry skin and prepare for an earthy delite. Pure essential oils of geranium rose, palmarosa, cedarwood and lavender calm the senses while increasing circulation and flushing impurities from the skin. Regain the luster your skin once had with the 地 tsuchi (Earth) Cleansing Body Scrub.

Use: Grab a small amount. Massage gently onto surface of dry skin. Add a small amount of warm water and massage gently again. Rinse with warm water, dry and apply 地 tsuchi (Earth) Body Lotion.

Ingredients: Sodium Chloride (Himalayan Pink Salt), Oryza Sativa (Rice) Bran Oil, Carthamus Tinctorius (Safflower) Seed Oil, Caprylic/Capric Triglyceride (Fractionated Coconut Oil), Lavandula Angustifolia (Lavender) Oil, Lavandula Angustifolia (Lavender) Buds, Jasminum Odoratissimum (Jasmine) Flowers, Pelargonium Capitatum X Radens (Rose Geranium) Oil, Tocopherol (Vitamin E), Cupressus Funebris (Chinese Cedarwood) Bark Oil, Centaurea Cyanus (Cornflower), Cymbopogon Martinii Var Motia (Palmarosa) Oil.
_________________________

水 mizu (Water) - Restore your skin’s natural radiance and clarity. 水 mizu (Water) Cleansing Body Scrub uses Japanese Sea salts (among the purest salts in the world) and Israeli Dead Sea salt (rich in nourishing minerals) to exfoliate and reveal refreshed skin. Soy seed aids in exfoliation and also provides lecithin and lipids for repairing and regenerating skin cells. As rosemary oil fights bacteria, improves circulation, and reduces the appearance of broken capillaries and varicose veins, protein-rich sweet almond oil nurtures and soothes. 水 mizu (Water) Cleansing Body Scrub also benefits skin with the anti-inflammatory, antiseptic, and uplifting properties of peppermint, spearmint, and thyme. Protect and replenish your skin with 水 mizu (Water) Cleansing Body Scrub.

Use: Grab a small amount. Massage gently onto surface of dry skin. Add a small amount of warm water and massage gently again. Rinse with warm water, dry and apply 水 mizu (Water) Body Lotion.

Ingredients: Sodium Chloride (Mediterranean Sea and Israeli Dead Sea Salt), Prunus Amygdalus Dulcis (Sweet Almond) Oil, Glycine Soja (Soy) Seeds, Rosmarinus Officinalis (Rosemary) Leaf Oil, Mentha Spicata (Spearmint) Leaf Oil, Mentha Piperita (Peppermint) Leaf, Thymus Zygis (Thyme) Oil, Urtica Dioica (Nettle) Leaf Powder, Tocopherol (Vitamin E).
_________________________

空 sora (Heaven) - Refresh and restore balance to your skin with natural exfoliants including organic evaporated cane sugar, luffa fruit powder, and lavender flower, 空 sora (Heaven) Cleansing Body Scrub rejuvenates dull, dry skin. Sweet almond oil, rich in proteins and vitamin D, nourishes and soothes while vitamin C-rich orange peel stimulates circulation and boosts collagen production. As the soft scent of lavender and patchouli oil calms and relaxes the mind, this scrub detoxifies skin, tones, and eases inflammation with orange oil and pink grapefruit oil. With tocopherol (vitamin E), it also helps diminish the signs of aging and protects skin from sun damage and pollutants. Reveal healthier, more balanced skin with our 空 sora (Heaven) Cleansing Body Scrub.

Use: Grab a small amount. Massage gently onto surface of dry skin. Add a small amount of warm water and massage gently again. Rinse with warm water, dry and apply 空 sora (Heaven) Body Lotion.

Ingredients: Organic Sucrose (Sugar), Prunus Amygdalus Dulcis (Sweet Almond) Oil, Citrus Sinensis (Orange) Peel Oil, Citrus Sinensis (Orange) Peel Powder, Luffa Cylindrica Fruit Powder, Lavandula Angustifolia (Lavender) Buds, Carthamus Tinctorius (Safflower) Powder, Citrus Grandis (Pink Grapefruit) Peel Oil, Lavandula Angustifolia (Lavender) Oil, Pogostemon Cablin (Patchouli) Oil, Tocopherol (Vitamin E).

Industry/Entity Type

Skin Care Product

Font styles to use
Other font styles liked:
• Helvetica Neue Slim for the logo VORELLE

Colors

Designer to choose colors to be used in the design.

Requirements
Must have
• My Labels must have the Japanese Kanji symbols for each of the elements characters. Must also have the brand name VORELLE on the label of each product.

```html
<!DOCTYPE html>
<html lang="en">
<head>
<meta charset="UTF-8">
<title>VORELLE Body Lotion Label</title>
<link rel="stylesheet" href="https://fonts.googleapis.com/css2?family=Jost:wght@300;400&display=swap">
<style>
  :root {
    --page: #ffffff;
    --label: #2e2824;
    --label-edge: #3a322d;
    --ink-light: #f1ece6;
    --gold: #d8b27a;
    --gold-soft: #c9a46e;
    --rule: rgba(216, 178, 122, 0.55);
  }
  * { margin: 0; padding: 0; box-sizing: border-box; }
  html, body {
    width: 1200px;
    height: 1200px;
    overflow: hidden;
    background: var(--page);
  }
  .canvas {
    position: relative;
    width: 1200px;
    height: 1200px;
    display: flex;
    align-items: center;
    justify-content: center;
  }
  .label {
    position: relative;
    width: 790px;
    height: 1030px;
    background: var(--label);
    border: 1px solid var(--label-edge);
    overflow: hidden;
    font-family: "Jost", "Helvetica Neue", Arial, sans-serif;
    color: var(--ink-light);
  }
  .backdrop-art {
    position: absolute;
    left: 70px;
    top: 620px;
    width: 520px;
    height: 410px;
    background: radial-gradient(ellipse at 50% 60%, rgba(255,255,255,0.05), rgba(255,255,255,0) 70%);
  }
  .brand {
    position: absolute;
    top: 140px;
    left: 0;
    width: 100%;
    text-align: center;
    font-weight: 300;
    font-size: 68px;
    letter-spacing: 4px;
    color: var(--ink-light);
  }
  .product-type {
    position: absolute;
    left: 92px;
    top: 330px;
    font-weight: 300;
    line-height: 1;
  }
  .product-type .kind {
    display: block;
    font-size: 58px;
    color: var(--gold);
  }
  .product-type .form {
    display: block;
    margin-top: 14px;
    font-size: 104px;
    letter-spacing: 1px;
    color: var(--ink-light);
  }
  .element-mark {
    position: absolute;
    left: 450px;
    top: 370px;
    width: 210px;
    height: 210px;
    background: linear-gradient(160deg, #dcb883, #c9a46e);
    opacity: 0.9;
  }
  .details {
    position: absolute;
    left: 94px;
    right: 94px;
    top: 740px;
  }
  .element-name {
    font-size: 22px;
    letter-spacing: 5px;
    color: var(--gold);
  }
  .ingredients {
    margin-top: 8px;
    font-size: 27px;
    line-height: 1.2;
    font-weight: 300;
    color: var(--ink-light);
  }
  .divider {
    margin: 18px 0 14px;
    height: 1px;
    background: var(--rule);
  }
  .tagline {
    font-size: 25px;
    font-weight: 300;
    color: var(--gold-soft);
  }
  .size {
    margin-top: 22px;
    text-align: center;
    font-size: 22px;
    font-weight: 300;
    color: var(--gold-soft);
  }
</style>
</head>
<body>
  <main class="canvas">
    <section class="label">
      <div class="backdrop-art" role="img" aria-label="Large faint element character watermark"></div>
      <h1 class="brand">VORELLE</h1>
      <p class="product-type">
        <span class="kind">body</span>
        <span class="form">lotion</span>
      </p>
      <div class="element-mark" role="img" aria-label="Gold element kanji emblem"></div>
      <div class="details">
        <p class="element-name">EMBER</p>
        <p class="ingredients">With warm amber resin, roasted rice bran &amp; golden safflower seed oil</p>
        <div class="divider"></div>
        <p class="tagline">Renew, smooth, and revive</p>
        <p class="size">8oz</p>
      </div>
    </section>
  </main>
</body>
</html>
```